Learn-to-Swim Program for Children's Day Camp (Walter Brightley Fieldgrounds)

We are a children's camp with a robust swim instruction program and we need a series of 5 kid-friendly banners which list the skills learned in our swim program that can be hung up around each outdoor pool complex. All together there are 6 overarching levels and 12 sublevels (see attached). Except for the Level V & VI, each banner should be one overarching level and the 2-3 sublevels that define it.

Each swim level has a name, most of which are sea creatures, and we want to have a corresponding image/avatar to go with the swim level name (e.g. tadpole, barracuda, orca, goldfish, catfish).

The banners should be 3 feet (width) by 5 feet (height). The banners will be hung outdoors so it needs a color scheme that won't get lost in the sunlight.

We will want to include our logo but do not need the design to match our logo colors. Logo can be in black or white.

Our website is: www.campwbf.example

Target Market(s)

children age 5 - 12

Industry/Entity Type

children's day camp

Requirements
Must have
• A progression from level I to level VI. Should have a happy, bright, fun, tone, text MUST be legible from at least a 5 foot distance
Should not have
• adult themes, a scheme that evokes sadness or fear

```html
<!DOCTYPE html>
<html lang="en">
<head>
<meta charset="utf-8">
<title>Wader Arc I – Splasher Arc I Banner</title>
<link href="https://fonts.googleapis.com/css2?family=Fredoka:wght@600;700&family=Patrick+Hand&display=swap" rel="stylesheet">
<style>
  :root {
    --backdrop: #e6e6e6;
    --paper: #ffffff;
    --leaf: #acd590;
    --leaf-title: #9ccf7e;
    --sky: #98b2de;
    --sky-title: #8aa4d8;
    --ink: #1c1c1c;
    --white: #ffffff;
    --water: #7fc4ea;
    --wave-tint: #dfe7f6;
  }
  * { margin: 0; padding: 0; box-sizing: border-box; }
  html, body {
    width: 1200px; height: 1200px; overflow: hidden;
    background: var(--backdrop);
  }
  .banner {
    position: absolute; left: 284px; top: 72px;
    width: 632px; height: 1055px;
    background: var(--paper);
    box-shadow: 0 2px 6px rgba(0,0,0,.18);
    overflow: hidden;
    font-family: "Patrick Hand", cursive;
    color: var(--ink);
  }
  .blobs { position: absolute; inset: 0; }
  .brand {
    position: absolute; left: 54px; top: 62px;
    display: flex; align-items: center; gap: 8px;
    font-size: 15px; color: var(--ink); letter-spacing: .3px;
  }
  .brand-mark { width: 14px; height: 14px; background: var(--ink); }
  .level-title {
    position: absolute; left: 54px;
    font-family: "Fredoka", sans-serif; font-weight: 700;
    line-height: 1; letter-spacing: 1px;
  }
  .level-title--wader { top: 177px; font-size: 56px; }
  .level-title--wader .word-a { color: var(--sky-title); }
  .level-title--wader .word-b { color: var(--leaf-title); }
  .level-title--splasher { top: 600px; font-size: 46px; color: var(--white); line-height: 1.1; }
  .skills-heading {
    position: absolute; left: 54px; font-size: 32px; font-weight: 400; letter-spacing: 1.5px;
  }
  .skills-heading--wader { top: 258px; }
  .skills-heading--splasher { top: 702px; color: var(--white); }
  .skill-list {
    position: absolute; left: 54px; list-style: none;
    font-size: 20px; line-height: 23.5px; letter-spacing: .5px;
  }
  .skill-list li::before { content: "> "; }
  .skill-list--wader { top: 302px; }
  .skill-list--splasher { top: 746px; color: var(--white); }
  .move-up-heading { position: absolute; font-size: 38px; font-weight: 400; line-height: 1; }
  .move-up-heading--wader { left: 54px; top: 444px; }
  .move-up-heading--splasher { right: 52px; top: 850px; }
  .move-up-text { position: absolute; font-size: 26px; line-height: 31px; letter-spacing: .6px; }
  .move-up-text--wader { left: 54px; top: 487px; }
  .move-up-text--splasher { right: 52px; top: 900px; text-align: right; }
  .swimmer-art {
    position: absolute; left: 264px; top: 440px; width: 368px; height: 170px;
    border-radius: 80px 0 0 60px;
    background: linear-gradient(160deg, #f3d2b8 0%, #6f86d6 40%, var(--water) 85%);
    opacity: .9;
  }
  .site-url {
    position: absolute; left: 54px; top: 988px;
    font-size: 16px; letter-spacing: 3px;
  }
  .wave-art {
    position: absolute; left: 276px; top: 993px; width: 319px; height: 29px;
    border-radius: 14px;
    background: var(--wave-tint);
  }
</style>
</head>
<body>
  <main class="banner">
    <svg class="blobs" width="632" height="1055" viewBox="0 0 632 1055" aria-hidden="true">
      <path fill="var(--leaf)" d="M632 98 C560 96 470 120 455 190 C440 250 400 270 380 330 C360 400 420 440 520 460 L632 470 Z"/>
      <path fill="var(--leaf)" d="M632 560 C520 560 420 610 360 700 C300 790 240 880 300 912 C380 940 520 930 632 915 Z"/>
      <path fill="var(--sky)" d="M0 590 C90 560 200 560 290 585 C370 607 430 640 520 690 C590 730 600 800 560 840 C500 890 380 870 260 875 C150 880 60 900 0 895 Z"/>
    </svg>

    <div class="brand"><span class="brand-mark"></span>Walter Brightley Fieldgrounds</div>

    <h1 class="level-title level-title--wader"><span class="word-a">WADER</span> <span class="word-b">ARC I</span></h1>
    <h2 class="skills-heading skills-heading--wader">SKILLS</h2>
    <ul class="skill-list skill-list--wader">
      <li>Gets into the water with assistance</li>
      <li>Follows pool rules</li>
      <li>Can hold big breath and get chin/ cheeks in water</li>
      <li>Cups hands to hold water and get some of face wet</li>
      <li>Doesn't always need assistance in water</li>
    </ul>
    <h3 class="move-up-heading move-up-heading--wader">Move-Up</h3>
    <p class="move-up-text move-up-text--wader">Must be comfortable<br>entering the water</p>

    <div class="swimmer-art" role="img" aria-label="Illustration of a child swimmer in cap and goggles doing front crawl through a splash"></div>

    <h1 class="level-title level-title--splasher">SPLASHER<br>ARC I</h1>
    <h2 class="skills-heading skills-heading--splasher">SKILLS</h2>
    <ul class="skill-list skill-list--splasher">
      <li>Enters and exits pool without assistance</li>
      <li>Can do a slide in entry</li>
      <li>Plays in water up to chest deep</li>
      <li>Dips face and head in water</li>
      <li>Blows bubbles through the mouth</li>
    </ul>
    <h3 class="move-up-heading move-up-heading--splasher">Move-Up</h3>
    <p class="move-up-text move-up-text--splasher">Must fully submerge body<br>and head underwater (no nose holding)</p>

    <p class="site-url">www.campwbf.example</p>
    <div class="wave-art" role="img" aria-label="Decorative wavy water lines"></div>
  </main>
</body>
</html>
```